70s 80s Revival club night

Hi,

I'm look for a poster design for a 70s & 80s revival club night.
The design must say thr following...

Copper Kites
70s & 80s Revival Club Night.

Also, must incorporate our company logo (Attached)

```html
<!DOCTYPE html>
<html lang="en">
<head>
<meta charset="utf-8">
<title>Copper Kites – 70's &amp; 80's Revival Club Night</title>
<link href="https://fonts.googleapis.com/css2?family=Bebas+Neue&family=Kaushan+Script&family=Alfa+Slab+One&family=Bungee&family=Oswald:wght@300;500;600&family=Montserrat:wght@300;500;600;700&display=swap" rel="stylesheet">
<style>
  :root {
    --ink: #050403;
    --gold: #e2b13c;
    --gold-glow: #c99a3e;
    --gold-deep: #5a4116;
    --red: #e8323a;
    --white: #ffffff;
  }
  * { margin: 0; padding: 0; box-sizing: border-box; }
  html, body { width: 750px; height: 1200px; overflow: hidden; background: var(--ink); }
  .poster {
    position: relative;
    width: 750px;
    height: 1200px;
    overflow: hidden;
    background: var(--ink);
    color: var(--white);
    text-align: center;
  }
  .poster__artwork {
    position: absolute;
    inset: 0;
    background:
      radial-gradient(ellipse 42% 24% at 50% 33%, rgba(255,236,190,0.8) 0%, rgba(201,154,62,0.45) 40%, transparent 80%),
      linear-gradient(180deg, #6b5220 0%, #8a6a2a 20%, #6a4e1c 36%, #3a2a10 46%, #140e06 54%, #070503 60%, #050403 78%, #0c0904 90%, #15100a 100%);
  }
  .title {
    position: absolute;
    left: 0; right: 0;
    top: 68px;
    font-family: "Bebas Neue", "Oswald", sans-serif;
    font-size: 246px;
    line-height: 1;
    letter-spacing: 0;
    color: var(--white);
    text-shadow: 4px 6px 10px rgba(0,0,0,0.45);
  }
  .title__script {
    position: absolute;
    left: 0; right: 0;
    top: 250px;
    font-family: "Kaushan Script", cursive;
    font-size: 150px;
    line-height: 1;
    color: var(--red);
    transform: rotate(-9deg);
    text-shadow: 3px 3px 0 var(--white), 6px 8px 10px rgba(0,0,0,0.35);
  }
  .decades {
    position: absolute;
    left: 0; right: 0;
    top: 640px;
    font-family: "Alfa Slab One", serif;
    font-size: 60px;
    line-height: 1;
    color: var(--white);
  }
  .decades__amp { color: var(--gold); font-size: 38px; margin: 0 10px; }
  .decades__tag {
    position: absolute;
    left: 0; right: 0;
    top: 716px;
    font-family: "Montserrat", sans-serif;
    font-weight: 500;
    font-size: 21px;
    letter-spacing: 17px;
    padding-left: 17px;
    color: var(--white);
  }
  .date {
    position: absolute;
    top: 788px;
    left: 0; right: 0;
    display: flex;
    justify-content: center;
    align-items: center;
    gap: 8px;
  }
  .date__day {
    font-family: "Bungee", sans-serif;
    font-size: 96px;
    line-height: 1;
    color: var(--red);
  }
  .date__details {
    text-align: left;
    font-family: "Oswald", sans-serif;
    line-height: 1;
  }
  .date__weekday { font-weight: 500; font-size: 36px; color: var(--white); }
  .date__month { font-weight: 300; font-size: 38px; color: var(--gold); }
  .date__time { font-weight: 500; font-size: 17px; color: var(--white); margin-top: 3px; }
  .features {
    position: absolute;
    top: 932px;
    left: 0; right: 0;
    display: flex;
    justify-content: center;
    gap: 36px;
    font-family: "Oswald", sans-serif;
    font-weight: 500;
    font-size: 18px;
    letter-spacing: 3px;
  }
  .features__divider { color: var(--gold); }
  .headliner {
    position: absolute;
    top: 968px;
    left: 0; right: 0;
    font-family: "Montserrat", sans-serif;
    font-size: 44px;
    line-height: 1;
  }
  .headliner__prefix { color: var(--gold); font-weight: 300; }
  .headliner__name { font-weight: 600; }
  .brand {
    position: absolute;
    top: 1076px;
    left: 0; right: 0;
    display: flex;
    justify-content: center;
    align-items: center;
    gap: 12px;
    font-family: "Montserrat", sans-serif;
    font-weight: 700;
    font-size: 30px;
    letter-spacing: 1px;
    color: var(--white);
  }
  .brand__dot { width: 24px; height: 24px; border-radius: 50%; background: var(--red); }
</style>
</head>
<body>
  <main class="poster">
    <div class="poster__artwork" role="img" aria-label="Golden sparkling disco lights glowing above a silhouetted dancing crowd, fading into a dark retro dance floor grid"></div>

    <h1 class="title">COPPER</h1>
    <p class="title__script">Kites</p>

    <p class="decades">70's<span class="decades__amp">&amp;</span>80's</p>
    <p class="decades__tag">REVIVAL CLUB NIGHT</p>

    <div class="date">
      <span class="date__day">23</span>
      <div class="date__details">
        <div class="date__weekday">SATURDAY</div>
        <div class="date__month">JANUARY</div>
        <div class="date__time">4PM - 9PM</div>
      </div>
    </div>

    <div class="features">
      <span>DRINK SPECIALS</span>
      <span class="features__divider">|</span>
      <span>DJ MIXER</span>
      <span class="features__divider">|</span>
      <span>DANCE PARTY</span>
    </div>

    <p class="headliner"><span class="headliner__prefix">DJ</span> <span class="headliner__name">WRENFIELD</span></p>

    <div class="brand">
      <span class="brand__dot"></span>
      <span>COPPER KITES</span>
    </div>
  </main>
</body>
</html>
```